Grace Fellowship Ardmore, MS needs a Business Card design

We are in the process of rebranding our church with a new logo with a fresh appeal to younger families moving into our community and joining our church. We are in need of a new business card design and would like to see 2 sided designs that incorporate the web color 00cccc.

We would like to have our logo, church name (grace fellowship ardmore) and our what we are about (gather.grow.serve.) in addition to the following information:
Name: Dr. Samuel Whitfield
Title: Teaching Pastor
Phone: 6015550142
Email: swhitfield@gfcardmore.example
Website: www.gfcardmore.example
Address: 714 N Elmwood Avenue Ardmore, MS 39187

Target Market(s)

Ardmore, MS is a bedroom community outside of Jackson that is experiencing exponential growth with young professionals/young families moving in. We are making a lot of changes to reach this demographic while still honoring and continuing to reach those who have lived here for a while.

Industry/Entity Type

Church

Contact Information for Business Card

Grace Fellowship Ardmore - gather.grow.serve.
Dr. Samuel Whitfield
Teaching Pastor
6015550142
swhitfield@gfcardmore.example
www.gfcardmore.example
714 N Elmwood Avenue
Ardmore, MS 39187

Font styles to use
Sans Serif

```html
<!DOCTYPE html>
<html lang="en">
<head>
<meta charset="utf-8">
<title>Grace Fellowship Ardmore – Business Card</title>
<link href="https://fonts.googleapis.com/css2?family=Lato:wght@400;700;900&display=swap" rel="stylesheet">
<style>
  :root {
    --stage: #1c1c1c;
    --card-dark: #121212;
    --card-light: #ececec;
    --teal: #2fb3a8;
    --teal-soft: #8fd6cf;
    --ink: #333333;
    --brand-grey: #8a8a8a;
    --tagline: #d8d8d8;
    --rule: #d4d4d4;
  }
  * { box-sizing: border-box; margin: 0; padding: 0; }
  html, body {
    width: 1200px; height: 900px; overflow: hidden;
    background: var(--stage);
    font-family: "Lato", sans-serif;
  }
  .stage {
    width: 1200px; height: 900px;
    display: flex; align-items: center; justify-content: center; gap: 40px;
  }
  .card {
    width: 540px; height: 309px;
    border-radius: 22px;
    position: relative;
    overflow: hidden;
  }
  /* Back side */
  .card-back {
    background: var(--card-dark);
    display: flex; flex-direction: column; align-items: center; justify-content: center;
  }
  .brand-mark {
    width: 92px; height: 92px; border-radius: 50%;
    background: var(--teal-soft);
    margin-bottom: 26px;
  }
  .brand-name {
    font-size: 19px; font-weight: 400; letter-spacing: 0.5px;
    color: var(--brand-grey); text-transform: uppercase;
  }
  .tagline {
    margin-top: 12px;
    font-size: 12px; letter-spacing: 1px;
    color: var(--tagline); text-transform: uppercase;
  }
  /* Front side */
  .card-front { background: var(--card-light); }
  .front-brand {
    position: absolute; right: 40px; top: 34px;
    display: flex; flex-direction: column; align-items: flex-end;
  }
  .front-brand .brand-mark {
    width: 62px; height: 62px; margin-bottom: 16px; margin-right: 80px;
  }
  .front-brand .brand-name { font-size: 15px; }
  .divider {
    position: absolute; left: 40px; right: 40px; top: 146px;
    height: 1px; background: var(--rule);
  }
  .person { position: absolute; left: 40px; top: 162px; }
  .person-name {
    font-size: 21px; font-weight: 900; color: var(--teal);
    text-transform: uppercase; letter-spacing: 0.3px;
  }
  .person-title { font-size: 15px; color: var(--ink); margin-top: 2px; }
  .contact-list { list-style: none; margin-top: 12px; padding-left: 14px; }
  .contact-list li {
    display: flex; align-items: center; gap: 8px;
    font-size: 15px; color: var(--ink); line-height: 21px;
  }
  .contact-list svg { width: 13px; height: 13px; flex: none; }
  .address {
    position: absolute; right: 40px; top: 162px;
    text-align: right; font-size: 15px; line-height: 20px; color: var(--ink);
    font-style: normal;
  }
</style>
</head>
<body>
<main class="stage">
  <section class="card card-back" aria-label="Card back">
    <div class="brand-mark"></div>
    <p class="brand-name">Grace Fellowship Ardmore</p>
    <p class="tagline">gather.grow.serve.</p>
  </section>

  <section class="card card-front" aria-label="Card front">
    <div class="front-brand">
      <div class="brand-mark"></div>
      <p class="brand-name">Grace Fellowship Ardmore</p>
    </div>
    <div class="divider"></div>

    <div class="person">
      <h1 class="person-name">Dr. Samuel Whitfield</h1>
      <p class="person-title">Teaching Pastor</p>
      <ul class="contact-list">
        <li>
          <svg viewBox="0 0 16 16" aria-hidden="true"><path fill="#2fb3a8" d="M3 1l3 3-1.5 2a9 9 0 0 0 5.5 5.5L12 10l3 3-2 2C7 15 1 9 1 3z"/></svg>
          6015550142
        </li>
        <li>
          <svg viewBox="0 0 16 16" aria-hidden="true"><rect x="1" y="3" width="14" height="10" rx="1" fill="#2fb3a8"/><path d="M1.5 3.5L8 9l6.5-5.5" fill="none" stroke="#ececec" stroke-width="1.4"/></svg>
          swhitfield@gfcardmore.example
        </li>
        <li>
          <svg viewBox="0 0 16 16" aria-hidden="true"><circle cx="8" cy="8" r="7" fill="#2fb3a8"/><path d="M1 8h14M8 1c-3 4-3 10 0 14M8 1c3 4 3 10 0 14" fill="none" stroke="#ececec" stroke-width="1"/></svg>
          www.gfcardmore.example
        </li>
      </ul>
    </div>

    <address class="address">
      714 N Elmwood Avenue<br>
      Ardmore, MS 39187
    </address>
  </section>
</main>
</body>
</html>
```